Infographic to communicate Cyber Security and Insurance Product Offering for IT Service Providers

We need an inspirational infographic that shows how TrellaWorks works with QDR (an MSP partner) to help organisations close the loop on cyber risk. The design should illustrate the layers of the IT infrastructure stack and the systems and processes that wrap around it to protect and mitigate against risk.
At the core: MSP Services (Desktop, Software, Website). Surrounding this: TrellaWorks Governance & Protection, leading into an Incident layer that connects to TrellaWorks Insurance and Incident Response, linked by a continuous feedback loop. The outer circle should represent the constant threat of cyber attack.
TrellaWorks core offerings for this graphic:
Plinth Verify (compliance/assurance product)
Plinth Cover
QDR Primary Services (directly connected to TrellaWorks):
Managed IT Services
Disaster Recovery as a Service (DRaaS)
E8 Security Packages
Cloud Hosting & Infrastructure
QDR Secondary Services (supporting but not directly anchored):
Telephony & Unified Communications
Networking Services
Data Backup & Storage Solutions
Professional Services & Consulting
Procurement & Licensing
Training & User Awareness
Style: Modern, professional, and client-friendly, with a technology-inspired colour palette.
Deliverables: Polished colour version plus editable source files — preferably in Figma, or alternatively if not possible using either Adobe Illustrator (.AI) or a layered Photoshop (.PSD) (e.g. industry standards for editable design).
Rewards: The winning design prize will be increased by $100, and we will also award $50 each to the 2nd and 3rd place runner-ups, as our way of giving a little more back.
A simple wireframe visual guide has been uploaded as a reference, but this should in no way limit or restrict your creativity. We encourage original, innovative approaches to bring this concept to life.
Ownership & Exclusivity: As per ArtMarquee’s T&Cs, all rights to the winning design will transfer to us once the project is complete for our ongoing use. We also kindly ask that the work created here remain exclusive to this project, meaning it won’t be reused or lightly modified for other clients in the future. The reason is simple: once we’ve invested in and paid for a design, we want to be confident it won’t turn up on a competitor’s website with just a different colour scheme. Thanks again for respecting that. [Note:- The designs submitted so far haven’t quite hit the mark, so I’ve put together a couple of slides to clarify direction. These outline the key stakeholders, the current IT services and challenges, how the Morvane product addresses those challenges, and a simple version of what we’d like the infographic to convey. Please review these slides carefully, as they should give you a clearer understanding of the story we want the design to tell.]
Target Market(s)
Small to Medium sized businesses
Colors
Designer to choose colors to be used in the design.
Look and feel

```html
<!DOCTYPE html>
<html lang="en">
<head>
<meta charset="utf-8">
<title>TrellaWorks – Closing the Loop on Cyber Risk</title>
<link href="https://fonts.googleapis.com/css2?family=Open+Sans:wght@600;700&display=swap" rel="stylesheet">
<style>
  :root {
    --backdrop: #a6fefd;
    --navy: #012570;
    --ring-top: #4af0e6;
    --ring-bottom: #2680ff;
    --core-top: #34aab5;
    --core-bottom: #0b4fa6;
    --msp-head: #22e3fc;
    --msp-outline: #6a4fc9;
    --row-desktop: #33b9bf;
    --row-software: #33b9bf;
    --row-website: #2289b0;
    --row-divider: #2494b5;
    --incident-box: #043e94;
    --step-box: #054399;
    --text: #ffffff;
  }
  html, body {
    margin: 0;
    padding: 0;
    width: 1200px;
    height: 1200px;
    overflow: hidden;
    background: var(--backdrop);
  }
  .infographic {
    display: block;
    width: 1200px;
    height: 1200px;
  }
  .label {
    font-family: "Open Sans", Arial, sans-serif;
    font-weight: 700;
    fill: var(--text);
    text-anchor: middle;
  }
  .threat-label { font-size: 40px; }
  .governance-title { font-size: 47px; }
  .msp-title {
    font-size: 37px;
    font-weight: 600;
    stroke: var(--msp-outline);
    stroke-width: 0.8px;
    paint-order: stroke;
  }
  .stack-label { font-size: 25px; }
  .incident-label { font-size: 30px; }
  .step-label { font-size: 22px; }
  .step-label.small { font-size: 21px; }
  .loop-line {
    fill: none;
    stroke: var(--text);
    stroke-width: 3.5;
    stroke-linecap: round;
    stroke-linejoin: round;
  }
</style>
</head>
<body>
<svg class="infographic" viewBox="0 0 1200 1200" xmlns="http://www.w3.org/2000/svg" role="img" aria-label="TrellaWorks cyber risk loop infographic">
  <defs>
    <linearGradient id="ringGradient" x1="0" y1="0" x2="0" y2="1">
      <stop offset="0" stop-color="var(--ring-top)"/>
      <stop offset="1" stop-color="var(--ring-bottom)"/>
    </linearGradient>
    <linearGradient id="coreGradient" x1="0" y1="0" x2="0" y2="1">
      <stop offset="0" stop-color="var(--core-top)"/>
      <stop offset="0.45" stop-color="#2a9db2"/>
      <stop offset="1" stop-color="var(--core-bottom)"/>
    </linearGradient>
    <path id="threatArc" d="M 289 537 A 311 311 0 0 1 911 537"/>
  </defs>

  <!-- Poster panel -->
  <rect class="panel" x="205" y="34" width="790" height="1144" fill="var(--navy)"/>

  <!-- Outer threat ring -->
  <circle class="threat-ring" cx="600" cy="537" r="328.5" fill="none" stroke="url(#ringGradient)" stroke-width="66"/>
  <text class="label threat-label">
    <textPath href="#threatArc" startOffset="50%" textLength="660" lengthAdjust="spacing">CONSTANT THREAT OF CYBER ATTACK</textPath>
  </text>

  <!-- Governance & protection layer -->
  <rect class="governance-layer" x="363" y="294" width="466" height="532" rx="168" fill="url(#coreGradient)"/>
  <text class="label governance-title" x="596" y="383">TRELLAWORKS</text>
  <text class="label governance-title" x="596" y="440">GOVERNANCE</text>
  <text class="label governance-title" x="596" y="498">&amp; PROTECTION</text>

  <!-- MSP services stack -->
  <g class="msp-stack">
    <rect x="470" y="522" width="252" height="284" rx="12" fill="var(--row-website)"/>
    <path d="M 470 652 V 534 Q 470 522 482 522 H 710 Q 722 522 722 534 V 652 Z" fill="var(--msp-head)"/>
    <rect x="470" y="652" width="252" height="49" fill="var(--row-desktop)"/>
    <rect x="470" y="701" width="252" height="2" fill="var(--row-divider)"/>
    <rect x="470" y="703" width="252" height="49" fill="var(--row-software)"/>
    <text class="label msp-title" x="596" y="579">QDR MSP</text>
    <text class="label msp-title" x="594" y="620">SERVICES</text>
    <text class="label stack-label" x="596" y="686">DESKTOP</text>
    <text class="label stack-label" x="596" y="735">SOFTWARE</text>
    <text class="label stack-label" x="596" y="790">WEBSITE</text>
  </g>

  <!-- Incident and response loop -->
  <rect class="incident-box" x="478" y="836" width="233" height="41" rx="4" fill="var(--incident-box)"/>
  <text class="label incident-label" x="595" y="866">INCIDENT</text>

  <path class="loop-line" d="M 478 861 C 440 867, 408 878, 390 892 C 370 906, 370 938, 392 954 C 415 972, 447 982, 473 987"/>
  <path class="loop-line" d="M 711 861 C 745 865, 770 874, 792 888 C 805 897, 810 908, 812 918"/>
  <path class="loop-line" d="M 802 917 L 812 928 L 823 917"/>
  <path class="loop-line" d="M 807 944 C 795 962, 765 978, 716 987"/>

  <rect class="step-box" x="473" y="902" width="244" height="72" rx="5" fill="var(--step-box)"/>
  <text class="label step-label" x="595" y="935">TRELLAWORKS</text>
  <text class="label step-label" x="595" y="961">INSURANCE</text>

  <rect class="step-box" x="469" y="997" width="256" height="62" rx="5" fill="var(--step-box)"/>
  <text class="label step-label small" x="595" y="1027">INCIDENT</text>
  <text class="label step-label small" x="595" y="1050">RESPONSE</text>
</svg>
</body>
</html>
```